Redesign of Leavely Calendar website

Looking to drastically improve our Leavely (paid time off) Calendar look and feel. Need a modern and well thought out design that is fun.
Current Screenshots
https://files.brinvola.net/sheet/d/7vRt2mWq9LpZa4XkeN8sBy3dHcJ0fUoT6iQgEwMnY/view?mode=sharing
It's written in PHP and Laravel, if that matters. I am not necessarily attached to any of the current design, so please go wild. Current functionality needs to remain the same, but some can be added if you feel it would be of value. Layout can certainly change.
NOTE - this calendar can be used by any company, not just our own. So we'd like it to have a look and feel that is easy to navigate.
Site logo is attached.
Pages needed:
* Login Page
* Registration Page
* Calendar page
* Add Leavely method
* Admin page (will use template for all admin areas)
* User profile page
Thanks!

```html
<!DOCTYPE html>
<html lang="en">
<head>
<meta charset="utf-8">
<title>Leavely – Sign in</title>
<link href="https://fonts.googleapis.com/css2?family=Poppins:wght@400;500;600;700&display=swap" rel="stylesheet">
<style>
  :root {
    --page-bg: #f9f9f9;
    --card-bg: #ffffff;
    --brand-blue: #0077c2;
    --ink: #3b4756;
    --muted: #a9afb6;
    --line: #dfe2e5;
    --field-border: #d3d6da;
  }
  * { box-sizing: border-box; margin: 0; padding: 0; }
  html, body {
    width: 1200px; height: 969px; overflow: hidden;
    background: var(--page-bg);
    font-family: "Poppins", sans-serif;
    color: var(--ink);
  }
  .stage { position: relative; width: 1200px; height: 969px; }

  .brand {
    position: absolute; left: 89px; top: 36px;
    display: flex; align-items: center; gap: 8px;
    font-size: 32px; font-weight: 700; color: var(--ink); letter-spacing: -0.5px;
  }
  .brand-dot { width: 34px; height: 34px; border-radius: 50%; background: var(--brand-blue); }

  .top-prompt {
    position: absolute; right: 89px; top: 44px;
    font-size: 16px; color: var(--ink);
  }
  .top-prompt a { color: var(--brand-blue); font-weight: 500; text-decoration: none; }

  .signin-card {
    position: absolute; left: 418px; top: 136px; width: 364px; height: 640px;
    background: var(--card-bg); border-radius: 6px;
    box-shadow: 0 2px 10px rgba(0,0,0,0.04);
  }
  .eyebrow {
    position: absolute; top: 48px; width: 100%; text-align: center;
    font-size: 16px; font-weight: 500; color: var(--brand-blue);
  }
  .headline {
    position: absolute; top: 68px; width: 100%; text-align: center;
    font-size: 28px; font-weight: 400; color: var(--ink);
  }
  .headline-rule {
    position: absolute; top: 116px; left: 162px; width: 39px; height: 2px; background: var(--brand-blue);
  }
  .continue-label {
    position: absolute; top: 144px; width: 100%; text-align: center;
    font-size: 17px; font-weight: 500;
  }
  .social-row {
    position: absolute; top: 188px; left: 62px; display: flex; gap: 10px;
  }
  .social-btn {
    width: 73px; height: 73px; border: 1.5px solid var(--line); border-radius: 5px;
    background: #fff; display: flex; align-items: center; justify-content: center;
    font-size: 11px; font-weight: 500; color: var(--ink);
  }
  .divider {
    position: absolute; top: 282px; left: 31px; width: 302px;
    display: flex; align-items: center; gap: 10px;
    font-size: 14px; color: var(--muted);
  }
  .divider::before, .divider::after { content: ""; flex: 1; height: 1px; background: var(--line); }

  .field {
    position: absolute; left: 29px; width: 304px; height: 55px;
    border: 1.5px solid var(--field-border); border-radius: 5px;
    padding-left: 21px; display: flex; align-items: center;
    font-size: 18px; color: var(--ink);
  }
  .field-email { top: 339px; }
  .field-password { top: 404px; }

  .remember {
    position: absolute; left: 30px; top: 474px;
    display: flex; align-items: center; gap: 10px; font-size: 15.5px;
  }
  .checkbox {
    width: 21px; height: 21px; border-radius: 4px; background: var(--brand-blue);
    display: flex; align-items: center; justify-content: center;
  }
  .forgot {
    position: absolute; right: 27px; top: 474px; text-align: right;
    font-size: 15.5px; line-height: 20px; color: var(--brand-blue); text-decoration: none;
  }
  .primary-btn {
    position: absolute; left: 29px; top: 534px; width: 304px; height: 56px;
    background: var(--brand-blue); border-radius: 5px; border: none;
    color: #fff; font-family: "Poppins", sans-serif; font-size: 19.5px; font-weight: 700;
    display: flex; align-items: center; justify-content: center;
  }
  .secondary-btn {
    position: absolute; left: 447px; top: 802px; width: 304px; height: 55px;
    border: 1.5px solid var(--field-border); border-radius: 5px; background: transparent;
    display: flex; align-items: center; justify-content: center;
    font-size: 18px; color: var(--brand-blue);
  }
</style>
</head>
<body>
<main class="stage">
  <div class="brand"><span>Leavely</span><span class="brand-dot"></span></div>
  <p class="top-prompt">You do not have an account? <a href="#">Sign up</a></p>

  <section class="signin-card">
    <p class="eyebrow">SIGN IN</p>
    <h1 class="headline">Welcome back</h1>
    <div class="headline-rule"></div>
    <p class="continue-label">Continue with...</p>
    <div class="social-row">
      <div class="social-btn">Friendo</div>
      <div class="social-btn">Searchly</div>
      <div class="social-btn">Searchly+</div>
    </div>
    <div class="divider">OR</div>
    <div class="field field-email">Email</div>
    <div class="field field-password">Password</div>
    <label class="remember">
      <span class="checkbox">
        <svg width="13" height="10" viewBox="0 0 13 10"><path d="M1.5 5 L5 8.5 L11.5 1.5" fill="none" stroke="#fff" stroke-width="2" stroke-linecap="round" stroke-linejoin="round"/></svg>
      </span>
      Remember me
    </label>
    <a class="forgot" href="#">Forgot your<br>password?</a>
    <div class="primary-btn">SIGN IN</div>
  </section>

  <div class="secondary-btn">Don't have an account?</div>
</main>
</body>
</html>
```